Flyer-Design für Open Workspace Lösung
Zielgruppe
Was machen wir? Open Workspace Lösung für Ärzte und Psychotherapeuten.
Zielgruppe: Unser Angebot richtet sich an Ärzte, Psychologen, Psychotherapeuten, Heilpraktiker für Psychotherapie (HeilprG) sowie Coaches und Supervisoren mit vergleichbarem und zertifiziertem Hintergrund. Darüber hinaus stehen die Räume auch für Seminare, Workshops oder Gruppenangebote zur Verfügung.
Aufgabenstellung
1. Die Word-Skizze ist ein Entwurf, der gerne verändert werden kann.
2. Das Foto in der oberen Hälfte ist ein Platzhalter. Es ist zwar real aber wir haben leider noch kein gutes Foto der fertigen Räume. Daher sollte, falls ein Bild verwendet wird, eine bearbeitbare Version mitgeliefert werden, damit wir das Bild noch austauschen können. Es muss kein Bild im Flyer verwendet werden, kann aber.
3. Unser Logo sollte auf den Flyer kommen. Es gibt das Logo mit und ohne Text. Beide hängen wir als Datei mit an.
4. Wir haben eine Website: www.praxis-sonnenwiese.de
Der Flyer sollte zu dieser passen. Die Schriftart der Website ist font-famliy: 'Lato', sans-serif und sollte verwendet werden.
5. Die Farbe (türkis) ist vorgegeben. Die Definition ist: #0CE0AE
Die Grautöne der Website sind folgende: #444444, #555444, #5A5A5A, #888888, #CCCCCC #F4F4F4
6. wir hätten gerne einen one-pager, den man als Werbung an Emails anhängen und im Internet veröffentlichen kann und einen Flyer, der ausgedruckt ausliegen kann

```html
<!DOCTYPE html>
<html lang="de">
<head>
<meta charset="utf-8">
<title>Praxis an der Sonnenwiese – Flexible Raummiete</title>
<link href="https://fonts.googleapis.com/css2?family=Lato:ital,wght@0,300;0,400;0,700;0,900;1,400;1,700&display=swap" rel="stylesheet">
<style>
  :root {
    --teal: #5cba9d;
    --ink-dark: #555555;
    --ink: #6a6a6a;
    --ink-soft: #888888;
    --paper: #ffffff;
    --stage: #dcdde0;
  }
  * { box-sizing: border-box; margin: 0; padding: 0; }
  html, body {
    width: 1200px; height: 848px; overflow: hidden;
    background: var(--stage);
    font-family: 'Lato', sans-serif;
  }
  .flyer {
    position: absolute; left: 317px; top: 24px;
    width: 566px; height: 800px;
    background: var(--paper);
    overflow: hidden;
  }
  .hero-photo {
    position: absolute; left: 0; top: 0; width: 566px; height: 211px;
    background: linear-gradient(180deg, #e9ece6 0%, #dfe3d8 40%, #d8d2c6 75%, #ece9e2 100%);
  }
  .side-band {
    position: absolute; left: 449px; top: 0; width: 94px; height: 800px;
    background: var(--teal);
  }
  .band-title {
    position: absolute; left: 8px; top: 28px; height: 590px;
    writing-mode: vertical-rl; transform: rotate(180deg);
    color: var(--paper); font-weight: 900; font-size: 46px;
    letter-spacing: 1px; line-height: 52px; text-align: left;
  }
  .band-subtitle {
    position: absolute; left: 58px; top: 40px; height: 280px;
    writing-mode: vertical-rl; transform: rotate(180deg);
    color: var(--paper); font-weight: 300; font-size: 23px;
    line-height: 28px; text-align: left;
  }
  .band-brand {
    position: absolute; left: 0; top: 650px; width: 94px;
    color: var(--paper);
  }
  .band-brand .brand-square {
    width: 40px; height: 40px; margin: 0 0 14px 4px;
    background: var(--paper);
  }
  .band-brand .brand-name {
    padding-left: 0; font-size: 13px; font-weight: 300;
    letter-spacing: 2px; line-height: 13.5px; text-transform: uppercase;
  }
  .content {
    position: absolute; left: 32px; width: 381px;
    color: var(--ink);
  }
  .main-title {
    top: 233px; font-style: italic; font-weight: 400; font-size: 22px;
    color: var(--ink-dark); letter-spacing: 0.2px;
  }
  .main-subtitle {
    top: 263px; font-style: italic; font-weight: 700; font-size: 14.5px;
    color: var(--ink-dark);
  }
  .section-title {
    font-style: italic; font-weight: 400; font-size: 15px; color: var(--ink-dark);
  }
  .copy p {
    font-size: 9px; line-height: 12.2px; text-align: justify;
    margin-bottom: 3px; font-weight: 400;
  }
  .copy strong { font-weight: 700; color: var(--ink-dark); }
  .contacts {
    position: absolute; top: 749px; left: 28px;
    display: flex; gap: 26px;
    font-size: 9px; line-height: 11.3px; color: var(--ink-soft);
  }
</style>
</head>
<body>
<main class="flyer">
  <div class="hero-photo" role="img" aria-label="Foto eines hellen Therapieraums mit zwei Sesseln, kleinem Tisch mit Blumen und Fenstern ins Grüne"></div>

  <aside class="side-band">
    <div class="band-title">Flexible Raummiete</div>
    <div class="band-subtitle">im Herzen von München</div>
    <div class="band-brand">
      <div class="brand-square"></div>
      <div class="brand-name">Praxis an der Sonnen&shy;wiese</div>
    </div>
  </aside>

  <h1 class="content main-title">PRAXIS AN DER SONNENWIESE</h1>
  <h2 class="content main-subtitle">Flexible Raummiete im Herzen von München</h2>

  <section class="content copy" style="top:285px">
    <p>Sie suchen schöne und hochwertig ausgestattete Räume in zentraler Lage für Therapie, Coaching oder Seminare? Sie möchten zeitlich flexibel arbeiten und Ihre monatlichen Fixkosten niedrig halten?</p>
    <p><strong>Unsere Praxis an der Sonnenwiese bietet Ihnen genau das.</strong></p>
  </section>

  <section class="content copy" style="top:349px">
    <h3 class="section-title">Die Praxis</h3>
    <p>Die Praxis liegt direkt am Lindenplatz, ist sehr ruhig und bietet einen wunderschönen Blick ins Grüne. In ihr stehen fünf frisch renovierte und hochwertig ausgestattete Therapieräume sowie zwei Seminarräume zur Verfügung.</p>
    <p>An welchem Tag, zu welcher Uhrzeit und für wie viele Stunden Sie diese mieten, können Sie entscheiden, ganz so wie es Ihr Bedarf von Woche zu Woche oder auch für das ganze Jahr verlangt.</p>
  </section>

  <section class="content copy" style="top:459px">
    <h3 class="section-title">Die Preise</h3>
    <p>Verschiedene Preismodelle bieten Ihnen je nach Bedarf volle Flexibilität. Sie können Räume entweder für einzelne Stunden oder im Abonnement mieten. Bei der Miete von einzelnen Stunden fallen keinerlei laufende Kosten an.</p>
    <p>Über ein Abonnement bieten wir Ihnen sehr attraktive Preise ab einer Stunde pro Woche. Sie können dadurch selbst bestimmen ob und in welcher Höhe Ihnen monatliche Fixkosten entstehen und welches Modell für Sie am besten geeignet ist.</p>
    <p>Die genauen Konditionen, Bilder und alle weiteren Informationen finden Sie auf der Website: <strong>www.praxis-sonnenwiese.de</strong></p>
  </section>

  <section class="content copy" style="top:597px">
    <h3 class="section-title">An wen richtet sich unser Angebot?</h3>
    <p>Unser Angebot richtet sich an Ärzte, Psychologen, Psychotherapeuten, Heilpraktiker für Psychotherapie (HeilprG) sowie Coaches und Supervisoren mit vergleichbarem und zertifiziertem Hintergrund. Darüber hinaus stehen die Räume auch für Seminare, Workshops oder Gruppenangebote zur Verfügung.</p>
  </section>

  <section class="content copy" style="top:681px">
    <p>Bei Fragen, für weitere Informationen oder zur Vereinbarung einer Besichtigung - gerne auch virtuell über Video - <strong>kontaktieren Sie uns:</strong></p>
  </section>

  <footer class="contacts">
    <address class="contact-card" style="font-style:normal">
      Carla Weidinger-Roth<br>kontakt@praxis-sonnenwiese.de<br>Tel.: 0176 48103927
    </address>
    <address class="contact-card" style="font-style:normal">
      Markus Roth<br>kontakt@praxis-sonnenwiese.de<br>Tel.: 0177 5390264
    </address>
  </footer>
</main>
</body>
</html>
```